Electrical Contracting Business card design

I would like a business card design for a new electrical business. I would like the print R.MOLT ELECTRICAL in large block lettering (spot gloss) on the front with atoms flying in a circle around the letter "A" of R.MOLT. Dark blue background, red lettering with the southern cross stars splashed in between the background and lettering.

On the rear of the card I would like the centre to have a box with 2 or 3 lines in it ( a space to write a time and date for the job to take place) surrounded by a big mass of confusing looking cables or a circuit diagram (something that would overwhelm people trying to make sense of it).

Thank you, I hope this isn't to detailed

Industry/Entity Type

Electrical

Contact Information for Business Card

R.MOLT ELECTRICAL
Phone: Brenn 0417853302
Brennr@mailvista.example
EC:47063

```html
<!DOCTYPE html>
<html lang="en">
<head>
<meta charset="utf-8">
<title>R.MOLT Electrical – Business Card</title>
<link rel="stylesheet" href="https://fonts.googleapis.com/css2?family=Open+Sans:wght@400;600&display=swap">
<style>
  :root {
    --backdrop: #3a3a3c;
    --card: #1b1b1c;
    --card-edge: #262628;
    --ink-light: #e6e6e6;
    --ink-muted: #9a9a9c;
    --brand-grey: #5c5d60;
    --accent-blue: #2f5fe0;
    --panel-grey: #c3c3c8;
    --trace-dark: #161617;
    --trace-light: #4a4a4e;
  }
  * { box-sizing: border-box; margin: 0; padding: 0; }
  html, body { width: 1200px; height: 849px; overflow: hidden; }
  body {
    background: var(--backdrop);
    font-family: "Open Sans", Arial, sans-serif;
    position: relative;
  }
  .card {
    position: absolute;
    width: 525px;
    height: 300px;
    border-radius: 22px;
    background: var(--card);
    border: 1px solid var(--card-edge);
    box-shadow: 0 18px 40px rgba(0,0,0,0.45);
    overflow: hidden;
  }
  .card--front { left: 50px; top: 120px; }
  .card--back { left: 625px; top: 430px; }

  /* Front */
  .brand {
    position: absolute;
    top: 62px;
    left: 0; right: 0;
    display: flex;
    justify-content: center;
    align-items: center;
    gap: 14px;
  }
  .brand__dot {
    width: 16px; height: 16px;
    border-radius: 50%;
    background: var(--accent-blue);
  }
  .brand__name {
    color: var(--brand-grey);
    font-weight: 600;
    font-size: 34px;
    letter-spacing: 2px;
  }
  .contact {
    position: absolute;
    left: 0; right: 0;
    top: 190px;
    display: flex;
    justify-content: center;
    align-items: stretch;
    gap: 18px;
  }
  .person { text-align: right; padding-top: 10px; }
  .person__name { color: var(--ink-light); font-size: 20px; line-height: 1.2; }
  .person__role { color: var(--ink-muted); font-size: 12px; }
  .divider { width: 2px; background: var(--ink-light); }
  .details { display: flex; flex-direction: column; gap: 8px; padding-top: 4px; }
  .details__row {
    display: flex; align-items: center; gap: 8px;
    color: var(--ink-light); font-size: 14px;
  }
  .details__icon { width: 16px; height: 16px; flex: none; }

  /* Back */
  .circuitry {
    position: absolute; inset: 0;
    background: radial-gradient(ellipse at 45% 45%, var(--trace-light) 0%, var(--trace-dark) 75%);
  }
  .job-panel {
    position: absolute;
    left: 120px; top: 70px;
    width: 285px; height: 150px;
    background: var(--panel-grey);
    padding: 30px 22px;
    display: flex; flex-direction: column; justify-content: space-between;
  }
  .job-panel__line { height: 2px; background: var(--accent-blue); }
</style>
</head>
<body>
  <section class="card card--front" aria-label="Card front">
    <div class="brand">
      <span class="brand__dot"></span>
      <span class="brand__name">R.MOLT ELECTRICAL</span>
    </div>
    <div class="contact">
      <div class="person">
        <p class="person__name">Brenn Lastname</p>
        <p class="person__role">Director</p>
      </div>
      <div class="divider"></div>
      <div class="details">
        <p class="details__row">
          <svg class="details__icon" viewBox="0 0 16 16" aria-hidden="true">
            <circle cx="8" cy="8" r="8" fill="#e6e6e6"/>
            <path d="M5.2 4.2l1.4-.4.9 2-1 .8c.5 1.1 1.3 1.9 2.4 2.4l.8-1 2 .9-.4 1.4c-3.2.2-6.3-2.9-6.1-6.1z" fill="#1b1b1c"/>
          </svg>
          0417853302
        </p>
        <p class="details__row">
          <svg class="details__icon" viewBox="0 0 16 16" aria-hidden="true">
            <circle cx="8" cy="8" r="8" fill="#e6e6e6"/>
            <rect x="4" y="5" width="8" height="6" rx="1" fill="#1b1b1c"/>
            <path d="M4.3 5.4L8 8.4l3.7-3" stroke="#e6e6e6" stroke-width="0.9" fill="none"/>
          </svg>
          Brennr@mailvista.example
        </p>
      </div>
    </div>
  </section>

  <section class="card card--back" aria-label="Card back">
    <div class="circuitry" role="img" aria-label="Dense circuit board traces surrounding a central chip"></div>
    <div class="job-panel" aria-label="Space to write job date and time">
      <div class="job-panel__line"></div>
      <div class="job-panel__line"></div>
      <div class="job-panel__line"></div>
    </div>
  </section>
</body>
</html>
```